KRV Business Cards

We are a local commercial development company based in Silicon Valley and we would like a new business card. I've attached a copy of our company brochure to give a flavor of what we do, our logo, info company colors/graphics, and our current business card. We don't necessarily need a crazy makeover, but would like something that feels a little bit more "fresh" and modern (we've had the same business card design for 15+ years), but still in keeping with our overall brand -- clean, high-quality, modern but timeless. Would like to add our website to the info on the card (www.lumbrel.com) and would like the flexibility for some folks to have an efax number listed and some not to have that included (without it looking like there is a hole).

```html
<!DOCTYPE html>
<html lang="en">
<head>
<meta charset="utf-8">
<title>KRV Business Cards</title>
<link rel="stylesheet" href="https://fonts.googleapis.com/css2?family=Cinzel:wght@400;500&family=Jost:wght@300;400&display=swap">
<style>
  :root {
    --navy: #34506b;
    --navy-deep: #2c465f;
    --rule: rgba(255, 255, 255, 0.28);
    --ink-light: #f3f5f7;
    --paper: #ffffff;
    --stage: #ecebe8;
    --grey-text: #4a4a4a;
  }
  * { box-sizing: border-box; margin: 0; padding: 0; }
  html, body { width: 1200px; height: 950px; overflow: hidden; background: var(--stage); }
  .canvas {
    width: 1200px; height: 950px;
    display: flex; flex-direction: column; align-items: center; justify-content: center; gap: 50px;
  }
  .card {
    width: 700px; height: 400px; position: relative;
    box-shadow: 0 6px 18px rgba(0, 0, 0, 0.15);
  }

  /* Front */
  .card-front { background: linear-gradient(110deg, #4a6580 0%, var(--navy) 45%, var(--navy-deep) 100%); color: var(--ink-light); }
  .frame { position: absolute; inset: 14px; border: 1px solid var(--rule); }
  .divider { position: absolute; left: 350px; top: 150px; width: 1px; height: 140px; background: rgba(255,255,255,0.55); }
  .company-name {
    position: absolute; left: 62px; bottom: 78px;
    font-family: "Cinzel", serif; font-size: 27px; line-height: 1.02; letter-spacing: 0.02em; font-weight: 400;
  }
  .company-name .suffix { font-size: 20px; }
  .contact { position: absolute; left: 392px; top: 60px; font-family: "Jost", sans-serif; }
  .person-name { font-family: "Cinzel", serif; font-size: 24px; letter-spacing: 0.03em; }
  .person-title { font-family: "Cinzel", serif; font-size: 13px; letter-spacing: 0.08em; margin-top: 2px; margin-bottom: 16px; }
  .address { font-size: 15px; font-weight: 300; line-height: 1.3; }
  .lines { list-style: none; margin-top: 4px; }
  .lines li { display: flex; align-items: center; gap: 9px; font-size: 15px; font-weight: 300; line-height: 1.3; }
  .lines svg { width: 12px; height: 12px; flex: none; }

  /* Back */
  .card-back { background: var(--paper); }
  .name-panel {
    position: absolute; left: 200px; top: 95px; width: 300px; height: 175px;
    background: var(--navy); color: var(--ink-light);
    display: flex; align-items: center; justify-content: center;
  }
  .name-panel .frame { inset: 9px; }
  .name-panel .company-name { position: static; font-size: 27px; }
  .web-line {
    position: absolute; left: 0; right: 0; bottom: 34px; text-align: center;
    font-family: "Jost", sans-serif; font-size: 13px; letter-spacing: 0.55em; color: var(--grey-text);
  }
</style>
</head>
<body>
<main class="canvas">
  <section class="card card-front">
    <div class="frame"></div>
    <h1 class="company-name">Kerrow<br>Ridge<br>Ventures, <span class="suffix">LLC</span></h1>
    <div class="divider"></div>
    <div class="contact">
      <p class="person-name">Nadia L. Verhoeven</p>
      <p class="person-title">Partner</p>
      <p class="address">218 Larkfield Avenue<br>Menlo Park, California 94025</p>
      <ul class="lines">
        <li><svg viewBox="0 0 12 12"><path d="M2 1l2 0 1 3-1.3 1a6 6 0 0 0 3.3 3.3L8 7l3 1v2a1 1 0 0 1-1 1A9 9 0 0 1 1 2a1 1 0 0 1 1-1z" fill="currentColor"/></svg>650.555.0142</li>
        <li><svg viewBox="0 0 12 12"><rect x="1" y="2" width="10" height="8" fill="none" stroke="currentColor" stroke-width="1.3"/></svg>650.555.0178</li>
        <li><svg viewBox="0 0 12 12"><rect x="3" y="0.5" width="6" height="11" rx="1" fill="currentColor"/><rect x="4" y="2" width="4" height="7" fill="#34506b"/></svg>650.555.0193</li>
        <li><svg viewBox="0 0 12 12"><rect x="1" y="1" width="10" height="10" fill="currentColor"/><path d="M3 6l2 2 4-4" fill="none" stroke="#34506b" stroke-width="1.5"/></svg>nadia@lumbrel.com</li>
        <li><svg viewBox="0 0 12 12"><circle cx="6" cy="6" r="5" fill="none" stroke="currentColor" stroke-width="1.2"/><path d="M1 6h10M6 1c-2.5 3-2.5 7 0 10M6 1c2.5 3 2.5 7 0 10" fill="none" stroke="currentColor" stroke-width="0.9"/></svg>www.lumbrel.com</li>
      </ul>
    </div>
  </section>

  <section class="card card-back">
    <div class="name-panel">
      <div class="frame"></div>
      <h2 class="company-name">Kerrow<br>Ridge<br>Ventures, <span class="suffix">LLC</span></h2>
    </div>
    <p class="web-line">www.lumbrel.com</p>
  </section>
</main>
</body>
</html>
```